Holiday Rental Company Flyer Design (DL not A5)

Note from PixelFolk Administration: The category sizing selected is A5, however the project requires DL sized artwork. Please refer to the DL template link below while the 'Special Requirements' are updated accordingly.

Project Brief:
We need a double sided DL flyer designed for an up market Holiday Rental Company that portrays a personalised approach to property management. These are to be used for letter box drops to homes we're specifically targeting so the design should be modern, complimentary colour palette, uncluttered & visually appealing.

Please Download the DL Template from Quillmark here: http://www.quillmark.com.au/qm/ns/propath/UploadResources.aspx?selectedTab=0?pfid=BFB&pf_id=BFB&xnav=easypath-upload-image#Templates

Target Market(s)

Wealthy Home Owners

Industry/Entity Type

It Company

Font styles to use
Other font styles liked:
• Avant Garde Extra Light & Demi

Colors
33b8a4

Requirements
Must have
• DL Flyer sizes (210mm width x 99mm width, plus 3mm bleed)
• Front: Logo, Main Image & Grab
• Back: Contact Details & Brief Description of our business
• Images: Ideally the main image should be the house with the pool but alternatively a lifestyle images could also be used.
Nice to have
• A creative designer!
Should not have
• Clutter & busy designs

```html
<!DOCTYPE html>
<html lang="en">
<head>
<meta charset="utf-8">
<title>Coastline Stays – DL Flyer</title>
<link href="https://fonts.googleapis.com/css2?family=Jost:wght@200;300;400;600&display=swap" rel="stylesheet">
<style>
  :root{
    --teal:#2fb59f;
    --teal-dark:#22a08b;
    --ink:#5d6166;
    --ink-soft:#8a8e93;
    --paper:#f4f4f4;
    --paper-edge:#dcdcdc;
    --stage:#ececec;
    --white:#ffffff;
  }
  *{box-sizing:border-box;margin:0;padding:0}
  html,body{width:1200px;height:849px;overflow:hidden;background:var(--stage)}
  body{font-family:"Jost",sans-serif;color:var(--ink)}
  .spread{position:absolute;left:28px;top:223px;display:flex;gap:4px}
  .flyer{position:relative;width:570px;height:403px;overflow:hidden;box-shadow:0 2px 8px rgba(0,0,0,.18)}

  /* front */
  .front-photo{position:absolute;inset:0;
    background:
      linear-gradient(180deg,rgba(255,255,255,0) 55%,rgba(0,0,0,.05) 100%),
      linear-gradient(160deg,#f4efe6 0%,#e9dcc6 30%,#d9c9a6 48%,#d8cf58 62%,#e7a255 80%,#5b86a8 100%);}
  .brand{position:absolute;left:16px;top:26px;font-weight:200;color:#6d6f73;
    font-size:33px;line-height:36px;letter-spacing:4px;text-transform:uppercase}
  .brand-dot{display:block;width:30px;height:30px;border:1.5px solid #8c8e92;border-radius:50%;margin:12px 0 0 78px}
  .tagline-band{position:absolute;left:0;right:0;top:334px;height:26px;background:rgba(255,255,255,.72);
    display:flex;align-items:center;justify-content:center;font-weight:300;font-size:15px;color:#555}

  /* back */
  .back{background:radial-gradient(ellipse at 50% 55%,#fbfbfb 0%,var(--paper) 55%,var(--paper-edge) 100%)}
  .photo-strip{position:absolute;left:0;top:0;width:570px;height:148px;display:block}
  .band{position:absolute;left:0;right:0;top:148px;height:30px;background:var(--teal);
    color:var(--white);font-weight:600;font-size:18px;line-height:30px;padding-left:24px}
  .copy{position:absolute;left:24px;right:18px;top:186px}
  .lead{font-size:10.5px;font-weight:300;line-height:15px;color:var(--ink-soft)}
  .feature{margin-top:9px;font-size:14.5px;font-weight:300;line-height:18px;color:var(--ink)}
  .feature strong{font-weight:600;color:#2c2f33}
  .points{list-style:none;margin-top:5px;font-size:10.5px;font-weight:300;line-height:15px;color:var(--ink)}
  .points li::before{content:"• "}
  .invite{margin-top:10px;text-align:center;font-size:9.5px;font-weight:300;color:var(--ink-soft)}
  .contacts{position:absolute;left:96px;top:340px;display:grid;grid-template-columns:220px 200px;row-gap:6px}
  .contact{display:flex;align-items:center;gap:8px;font-size:10px;font-weight:300;color:var(--ink-soft)}
  .contact.phone{font-size:22px;color:var(--ink);line-height:22px}
  .icon{width:16px;height:16px;background:var(--teal);border-radius:2px;flex:none;display:flex;align-items:center;justify-content:center}
  .icon svg{width:11px;height:11px;fill:var(--white)}
</style>
</head>
<body>
<main class="spread">
  <section class="flyer front">
    <div class="front-photo" role="img" aria-label="Bedroom with timber bedhead, yellow knitted cushions and a bright geometric quilt"></div>
    <div class="brand">Coastline<br>Stays<span class="brand-dot"></span></div>
    <div class="tagline-band">Holiday Rental Management with a difference.</div>
  </section>

  <section class="flyer back">
    <svg class="photo-strip" viewBox="0 0 570 148" preserveAspectRatio="none">
      <defs>
        <linearGradient id="house" x1="0" y1="0" x2="0" y2="1">
          <stop offset="0" stop-color="#3b3f8f"/><stop offset=".6" stop-color="#7b5fb0"/><stop offset="1" stop-color="#2c8fd0"/>
        </linearGradient>
        <linearGradient id="sea" x1="0" y1="0" x2="1" y2="1">
          <stop offset="0" stop-color="#3fc3c6"/><stop offset="1" stop-color="#1d8fa6"/>
        </linearGradient>
        <linearGradient id="bay" x1="0" y1="0" x2="0" y2="1">
          <stop offset="0" stop-color="#bcd9ee"/><stop offset=".6" stop-color="#e6eef2"/><stop offset=".62" stop-color="#5fb3cf"/><stop offset="1" stop-color="#3c97bd"/>
        </linearGradient>
      </defs>
      <polygon points="0,0 203,0 156,148 0,148" fill="url(#house)" role="img" aria-label="Modern house with lit swimming pool at dusk"/>
      <polygon points="209,0 408,0 361,148 162,148" fill="url(#sea)" role="img" aria-label="Seals swimming in clear turquoise water"/>
      <polygon points="414,0 570,0 570,148 367,148" fill="url(#bay)" role="img" aria-label="Sailing boat moored on a calm bay"/>
    </svg>
    <div class="band">What we do differently!</div>
    <div class="copy">
      <p class="lead">Rather than relying upon a key safe or a central pick-up destination, a ‘Coastline Stays’ staff member will greet guests upon arrival.</p>
      <p class="feature">Our <strong>‘Meet &amp; Greet’</strong> service provides home owners with an increased level of Security and also allows us to:</p>
      <ul class="points">
        <li>Prepare the home for their arrival (lights, heaters, music etc.)</li>
        <li>Establish a rapport &amp; help facilitate future bookings</li>
        <li>Reiterate their responsibilities to ensure the return of their bond</li>
      </ul>
      <p class="invite">If you’d like to know what your property could achieve or require additional information, please contact us on:</p>
    </div>
    <div class="contacts">
      <div class="contact phone"><span class="icon"><svg viewBox="0 0 24 24"><path d="M6.6 10.8a15 15 0 0 0 6.6 6.6l2.2-2.2c.3-.3.7-.4 1-.2 1.1.4 2.3.6 3.6.6.6 0 1 .4 1 1V20c0 .6-.4 1-1 1A17 17 0 0 1 3 4c0-.6.4-1 1-1h3.5c.6 0 1 .4 1 1 0 1.3.2 2.5.6 3.6.1.3 0 .7-.2 1z"/></svg></span>03.5123.4678</div>
      <div class="contact"><span class="icon"><svg viewBox="0 0 24 24"><path d="M12 2a10 10 0 1 0 4.5 18.9l-.9-1.8A8 8 0 1 1 20 12v1.2a1.8 1.8 0 0 1-3.6 0V7h-2v1a5 5 0 1 0 .6 7.5 3.8 3.8 0 0 0 7-2.3V12A10 10 0 0 0 12 2zm0 13a3 3 0 1 1 0-6 3 3 0 0 1 0 6z"/></svg></span>coastlinestays.com.au</div>
      <div class="contact"><span class="icon"><svg viewBox="0 0 24 24"><path d="M2 5h20v14H2zm2 2v.5l8 5 8-5V7zm0 2.8V17h16V9.8l-8 5z"/></svg></span>stay@coastlinestays.com.au</div>
      <div class="contact"><span class="icon"><svg viewBox="0 0 24 24"><path d="M12 2a7 7 0 0 0-7 7c0 5 7 13 7 13s7-8 7-13a7 7 0 0 0-7-7zm0 9.5A2.5 2.5 0 1 1 12 6.5a2.5 2.5 0 0 1 0 5z"/></svg></span>PO Box 18, Seaview Victoria 3900</div>
    </div>
  </section>
</main>
</body>
</html>
```